Geschäftspapiere
Zielgruppe
Die TIVA Salbe gibt ein zuverlässige Gefühl, durch ein innovatives Naturprodukt erstaunlich schnelle, wirkungsvolle Hilfe bei Schmerzen des Bewegungsapparates und bei Hautschäden zu erhalten und dabei gleichzeitig die Haut zu pflegen.
Wir wollen jetzt stärker auf die Zielgruppe TCM Praxis, Chiropraktiker, Physiotherapie gehen und wollen nun eine Preisliste dafür erstellen.
Aufgabenstellung
Zielgruppe ist B2B, TCM Praxis, Chiropraktiker, Physiotherapie.
Die Preisliste sollte auf den Briefpapier erstellt werden. Bitte an Farben, Logos etc. von der Webseite nehmen.

```html
<!DOCTYPE html>
<html lang="de">
<head>
<meta charset="utf-8">
<title>Preisliste – TIVA Naturbalsame</title>
<link rel="stylesheet" href="https://fonts.googleapis.com/css2?family=Heebo:wght@400;500;700&family=Source+Sans+3:wght@400;600&display=swap">
<style>
  :root {
    --bg: #d9d9d9;
    --paper: #f4f4f3;
    --ink: #161616;
    --grey: #555;
    --orange: #eda012;
    --orange-deep: #e47410;
    --yellow: #f5c23a;
    --red: #c40f0c;
    --white: #ffffff;
  }
  * { box-sizing: border-box; margin: 0; padding: 0; }
  html, body { width: 1200px; height: 1200px; overflow: hidden; background: var(--bg); }
  body { font-family: "Heebo", sans-serif; color: var(--ink); }

  .sheet {
    position: absolute; left: 176px; top: 0; width: 848px; height: 1200px;
    background: var(--paper); overflow: hidden;
    border-right: 8px solid var(--orange);
  }

  .sender {
    position: absolute; left: 96px; top: 176px;
    font-family: "Source Sans 3", sans-serif; font-size: 10px; color: var(--grey);
  }
  .sender b { font-weight: 600; color: #333; }
  .sender .dot { color: var(--orange); }

  .brand-disc {
    position: absolute; right: 40px; top: -150px; width: 300px; height: 300px;
    border-radius: 50%; background: var(--paper);
    box-shadow: 0 8px 10px -4px rgba(0,0,0,.25);
  }
  .brand {
    position: absolute; right: 80px; top: 60px; text-align: center; width: 230px;
  }
  .brand-name { display: flex; align-items: center; justify-content: center; gap: 10px;
    font-size: 52px; font-weight: 700; color: var(--ink); line-height: 1; }
  .brand-mark { width: 34px; height: 34px; border-radius: 50%; background: var(--orange); }
  .brand-sub { font-size: 14px; letter-spacing: 4px; color: #333; margin-top: 6px; }
  .brand-tag { font-size: 14px; font-weight: 700; letter-spacing: 2px; color: var(--orange); margin-top: 6px; }

  .title { position: absolute; top: 370px; left: 0; width: 100%; text-align: center;
    font-size: 34px; font-weight: 500; }
  .intro { position: absolute; top: 420px; left: 120px; width: 610px; text-align: center;
    font-size: 15px; line-height: 1.45; }

  .tiers { position: absolute; top: 530px; left: 92px; display: flex; gap: 38px; }
  .tier {
    position: relative; width: 196px; height: 345px; border-radius: 22px; overflow: hidden;
    background: linear-gradient(160deg, #f2a40c 0%, #f6c43c 45%, #efa211 70%, #eb9410 100%);
    box-shadow: 0 6px 10px rgba(0,0,0,.25);
  }
  .tier::before {
    content: ""; position: absolute; left: -40px; top: 110px; width: 90px; height: 80px;
    background: radial-gradient(circle, rgba(214,40,10,.8), transparent 70%);
  }
  .tier-icon {
    position: absolute; top: 30px; left: 60px; width: 76px; height: 76px; border-radius: 50%;
    border: 2px solid var(--white);
    background: radial-gradient(circle at 50% 55%, #f7c26a 0%, #e8641a 55%, #d9560e 100%);
  }
  .tier-dome {
    position: absolute; top: 130px; left: -22px; width: 240px; height: 300px; border-radius: 50%;
    border: 3px solid var(--white);
  }
  .tier-ring { position: absolute; top: 158px; left: 38px; }
  .tier-price { position: absolute; top: 168px; width: 100%; text-align: center;
    font-size: 30px; color: var(--white); }
  .tier-qty { position: absolute; top: 250px; width: 100%; text-align: center;
    font-size: 19px; color: var(--white); }
  .tier-label { position: absolute; bottom: 0; left: 0; width: 100%; height: 50px;
    border-top: 1px solid rgba(255,255,255,.7);
    display: flex; align-items: center; justify-content: center;
    font-size: 19px; font-weight: 700; letter-spacing: 1px; color: var(--white); }

  .tier--starter .tier-dome { background: linear-gradient(180deg, #f0bc3e, #eea818); }
  .tier--starter .tier-label { background: var(--yellow); }
  .tier--premium .tier-dome { background: linear-gradient(180deg, #e8780f, #ee9c14 70%); }
  .tier--premium .tier-label { background: var(--orange-deep); }
  .tier--special .tier-dome { background: linear-gradient(180deg, #b8080a, #e8601a 50%, #f0a015 75%); }
  .tier--special .tier-label { background: var(--red); }

  .body-copy { position: absolute; top: 905px; left: 85px; width: 680px;
    font-size: 14px; line-height: 1.5; }

  .footer {
    position: absolute; left: 0; bottom: 0; width: 100%; height: 118px; background: var(--orange);
    display: flex; padding: 22px 40px 0; gap: 24px;
    font-family: "Source Sans 3", sans-serif; font-size: 10.5px; line-height: 1.6; color: var(--white);
  }
  .footer-col { padding-right: 24px; }
  .footer-col + .footer-col { border-left: 2px solid var(--white); padding-left: 14px; }
  .footer b { font-weight: 600; }
  .footer dl { display: grid; grid-template-columns: 52px auto; column-gap: 8px; }
  .footer dt { font-weight: 600; }
</style>
</head>
<body>
<main class="sheet">
  <p class="sender"><b>Kellner Medizin Vertrieb GmbH</b> <span class="dot">-</span> Lindenweg 14 <span class="dot">-</span> 80331 München</p>

  <div class="brand-disc"></div>
  <header class="brand">
    <div class="brand-name"><span class="brand-mark"></span>TIVA</div>
    <div class="brand-sub">NATURBALSAME</div>
    <div class="brand-tag">LUMEN TIVA</div>
  </header>

  <h1 class="title">Preisliste</h1>
  <p class="intro">Lorem ipsum dolor sit amet, consectetuer adipiscing elit, sed diam nonummy nibh euismod tincidunt ut laoreet dolore magna aliquam erat volutpat. Ut wisi enim ad</p>

  <section class="tiers">
    <article class="tier tier--starter">
      <div class="tier-icon" role="img" aria-label="Lotusblüten-Symbol"></div>
      <div class="tier-dome"></div>
      <svg class="tier-ring" width="120" height="70" viewBox="0 0 120 70"><path d="M2 2 A58 58 0 0 0 118 2" fill="none" stroke="#fff" stroke-width="2.5"/></svg>
      <div class="tier-price">70,-</div>
      <div class="tier-qty">5 Tuben</div>
      <div class="tier-label">STARTER</div>
    </article>
    <article class="tier tier--premium">
      <div class="tier-icon" role="img" aria-label="Lotusblüten-Symbol"></div>
      <div class="tier-dome"></div>
      <svg class="tier-ring" width="120" height="70" viewBox="0 0 120 70"><path d="M2 2 A58 58 0 0 0 118 2" fill="none" stroke="#fff" stroke-width="2.5"/></svg>
      <div class="tier-price">300,-</div>
      <div class="tier-qty">20 Tuben</div>
      <div class="tier-label">PREMIUM</div>
    </article>
    <article class="tier tier--special">
      <div class="tier-icon" role="img" aria-label="Lotusblüten-Symbol"></div>
      <div class="tier-dome"></div>
      <svg class="tier-ring" width="120" height="70" viewBox="0 0 120 70"><path d="M2 2 A58 58 0 0 0 118 2" fill="none" stroke="#fff" stroke-width="2.5"/></svg>
      <div class="tier-price">500,-</div>
      <div class="tier-qty">50 Tuben</div>
      <div class="tier-label">SPECIAL</div>
    </article>
  </section>

  <p class="body-copy">Lorem ipsum dolor sit amet, consectetuer adipiscing elit, sed diam nonummy nibh euismod tincidunt ut laoreet dolore magna aliquam erat volutpat. Ut wisi enim ad Lorem ipsum dolor sit amet, consectetuer adipiscing elit, sed diam nonummy nibh euismod tincidunt ut laoreet dolore magna aliquam erat volutpat. Ut wisi enim ad minim.</p>

  <footer class="footer">
    <div class="footer-col">
      <b>Kellner Medizin Vertrieb GmbH</b><br>Lindenweg 14<br>80331 München<br>Deutschland
    </div>
    <div class="footer-col">
      <dl>
        <dt>Telefon:</dt><dd>0049 89 120 340 56</dd>
        <dt>Telefax:</dt><dd>0049 89 120 340 57</dd>
        <dt>E-Mail:</dt><dd>bestellung@kellner-medizin.de</dd>
      </dl>
    </div>
    <div class="footer-col">
      <b>Gesellschafter:</b> Jonas Weber<br>Amtsgericht München HRB 104 233
    </div>
  </footer>
</main>
</body>
</html>
```